Business Card Design

I need a business card for my baking business. Name of the company is Whisked by Tessa. I specialize in cookies and pies.
I don't make cupcakes or cakes. I would like a design with colors of brown, light pink and dark pink and maybe have the half eaten cookie be the dot of the "I" in my name. (Half eaten chocolate chip and the chips being hot pink light pink and brown chips).. I would like the card fun and modern design.
On the back of the card tag line- let me bake your day

Industry/Entity Type

Business

Contact Information for Business Card

Tessa Mernholt
Cell 5093617284
Email-Tesmern47@quillpost.net

```html
<!DOCTYPE html>
<html lang="en">
<head>
<meta charset="utf-8">
<title>Whisked by Tessa – Business Cards</title>
<link rel="stylesheet" href="https://fonts.googleapis.com/css2?family=Open+Sans:wght@300;400;600&display=swap">
<style>
  :root {
    --backdrop: #ecd3a9;
    --card-brown: #5a3c11;
    --brand-pink: #f45c5c;
    --text-light: #ffffff;
    --icon-dark: #111111;
  }
  html, body {
    margin: 0;
    padding: 0;
    width: 1200px;
    height: 993px;
    overflow: hidden;
    background: var(--backdrop);
    font-family: "Open Sans", sans-serif;
  }
  .canvas {
    position: relative;
    width: 1200px;
    height: 993px;
  }
  .card {
    position: absolute;
    width: 700px;
    height: 423px;
    background: var(--card-brown);
    box-shadow: 3px 4px 6px rgba(0, 0, 0, 0.35);
    overflow: hidden;
  }
  .card--plain { left: 46px; top: 73px; }
  .card--banded { left: 450px; top: 519px; }

  .brand-band {
    position: absolute;
    left: 168px;
    top: 0;
    width: 360px;
    height: 153px;
    background: var(--brand-pink);
  }
  .brand-name {
    position: absolute;
    left: 0;
    width: 100%;
    top: 80px;
    margin: 0;
    text-align: center;
    font-weight: 600;
    font-size: 42px;
    line-height: 50px;
    color: var(--brand-pink);
  }
  .brand-band .brand-name {
    top: 78px;
    font-size: 36px;
    color: var(--text-light);
  }
  .person-name {
    position: absolute;
    left: 0;
    width: 100%;
    top: 182px;
    margin: 0;
    text-align: center;
    font-weight: 300;
    font-size: 44px;
    line-height: 54px;
    color: var(--text-light);
  }
  .contact {
    position: absolute;
    top: 345px;
    display: flex;
    align-items: center;
    gap: 9px;
    font-weight: 300;
    font-size: 21px;
    line-height: 26px;
    color: var(--text-light);
  }
  .contact--phone { left: 87px; }
  .contact--email { left: 372px; }
  .contact-icon { width: 22px; height: 22px; flex: none; }
</style>
</head>
<body>
<main class="canvas">

  <section class="card card--plain">
    <h1 class="brand-name">Whisked by Tessa</h1>
    <p class="person-name">Tessa Mernholt</p>
    <div class="contact contact--phone">
      <span>5093617284</span>
      <svg class="contact-icon" viewBox="0 0 22 22" aria-hidden="true">
        <rect width="22" height="22" fill="var(--brand-pink)"/>
        <circle cx="11" cy="11" r="8" fill="var(--icon-dark)"/>
        <path d="M8 6.5 L9.6 6.2 L10.3 8.6 L9.4 9.4 Q10.2 11.6 12.4 12.6 L13.2 11.7 L15.6 12.4 L15.3 14 Q14.6 15.2 13 15 Q7.4 13.4 6.8 8 Q6.8 7 8 6.5 Z" fill="var(--text-light)"/>
      </svg>
    </div>
    <div class="contact contact--email">
      <span>Tesmern47@quillpost.net</span>
      <svg class="contact-icon" viewBox="0 0 22 22" aria-hidden="true">
        <rect width="22" height="22" fill="var(--brand-pink)"/>
        <circle cx="11" cy="11" r="8" fill="var(--icon-dark)"/>
        <rect x="6.5" y="8" width="9" height="6" fill="var(--text-light)"/>
        <path d="M6.5 8 L11 11.5 L15.5 8" fill="none" stroke="var(--icon-dark)" stroke-width="0.9"/>
      </svg>
    </div>
  </section>

  <section class="card card--banded">
    <div class="brand-band">
      <h1 class="brand-name">Whisked by Tessa</h1>
    </div>
    <p class="person-name">Tessa Mernholt</p>
    <div class="contact contact--phone">
      <span>5093617284</span>
      <svg class="contact-icon" viewBox="0 0 22 22" aria-hidden="true">
        <rect width="22" height="22" fill="var(--brand-pink)"/>
        <circle cx="11" cy="11" r="8" fill="var(--icon-dark)"/>
        <path d="M8 6.5 L9.6 6.2 L10.3 8.6 L9.4 9.4 Q10.2 11.6 12.4 12.6 L13.2 11.7 L15.6 12.4 L15.3 14 Q14.6 15.2 13 15 Q7.4 13.4 6.8 8 Q6.8 7 8 6.5 Z" fill="var(--text-light)"/>
      </svg>
    </div>
    <div class="contact contact--email">
      <span>Tesmern47@quillpost.net</span>
      <svg class="contact-icon" viewBox="0 0 22 22" aria-hidden="true">
        <rect width="22" height="22" fill="var(--brand-pink)"/>
        <circle cx="11" cy="11" r="8" fill="var(--icon-dark)"/>
        <rect x="6.5" y="8" width="9" height="6" fill="var(--text-light)"/>
        <path d="M6.5 8 L11 11.5 L15.5 8" fill="none" stroke="var(--icon-dark)" stroke-width="0.9"/>
      </svg>
    </div>
  </section>

</main>
</body>
</html>
```